Business Card Design for Event Planning Company

Create a business card for event planning company using our new logo. After I pick the design, I will need files made for 6 employees. Our company provides event design & logistics services as well as venue management. The font should be sans serif and complementary to the logo. I will need to know the name of the font selected for the final design. The phone numbers listed should be separated by "." not "-"

Address for the card
PO Box 318, Washington, DC 20019

Card One
Lorna Pettibone
lpettibone@galavoyant.com
202.481.7730

Card Two
Miriam Okonkwo
mokonkwo@galavoyant.com
202.556.2047

Card Three
Tessa Varnholt
tvarnholt@galavoyant.com
978.620.4471

Card Four
Robin Fess
rfess@galavoyant.com
202.718.3362

Card Five
Ada-Rose Pelletan-Uzor
adarose@galavoyant.com
202.839.1205

Card Six
Beatrix Holloway
Beatrix@galavoyant.com
202.492.6618

Target Market(s)

Corporate/Non-Profit

Industry/Entity Type

Event Planning

Contact Information for Business Card

Address for the card

Card One
Lorna Pettibone
lpettibone@galavoyant.com
202.481.7730

Card Two
Miriam Okonkwo
202.556.2047

Card Three
Tessa Varnholt
978.620.4471

Card Four
Robin Fess
rfess@galavoyant.com
202.718.3362

Card Five
Ada-Rose Pelletan-Uzor
202.839.1205

Card Six
Beatrix Holloway
202.492.6618

Font styles to use
Sans Serif

Colors

Designer to choose colors to be used in the design.

Requirements
Must have
• Two-sided with logo
Should not have
• Extra colors or be too busy

```html
<!DOCTYPE html>
<html lang="en">
<head>
<meta charset="utf-8">
<title>Galavoyant Business Card</title>
<link rel="stylesheet" href="https://fonts.googleapis.com/css2?family=Questrial&family=Source+Sans+3:wght@400;700&display=swap">
<style>
  :root {
    --backdrop: #e9e7e4;
    --card: #ffffff;
    --teal: #5fa3a1;
    --ink: #262626;
    --white: #ffffff;
  }
  * { box-sizing: border-box; margin: 0; padding: 0; }
  html, body {
    width: 1200px; height: 960px; overflow: hidden;
    background: var(--backdrop);
  }
  .sheet {
    width: 1200px; height: 960px;
    display: flex; flex-direction: column; align-items: center; justify-content: center;
    gap: 64px;
  }
  .card {
    position: relative;
    width: 600px; height: 343px;
    background: var(--card);
    box-shadow: 0 2px 10px rgba(0,0,0,0.12);
    overflow: hidden;
  }
  .brand {
    display: flex; align-items: center; justify-content: center; gap: 14px;
    font-family: "Questrial", sans-serif;
    color: var(--ink);
    letter-spacing: 0.5px;
  }
  .brand-dot {
    border-radius: 50%;
    background: var(--teal);
    flex: none;
  }
  /* front */
  .card-front .brand { position: absolute; left: 0; right: 0; top: 110px; font-size: 52px; }
  .card-front .brand-dot { width: 34px; height: 34px; }
  .website {
    position: absolute; left: 0; right: 0; top: 206px;
    text-align: center;
    font-family: "Questrial", sans-serif;
    font-size: 17px; letter-spacing: 4px;
    color: var(--ink);
  }
  /* back */
  .card-back .brand { position: absolute; left: 0; right: 0; top: 48px; font-size: 48px; }
  .card-back .brand-dot { width: 30px; height: 30px; }
  .holder-name {
    position: absolute; left: 0; right: 0; top: 132px;
    text-align: center;
    font-family: "Source Sans 3", sans-serif;
    font-weight: 700; font-size: 23px;
    color: var(--teal);
  }
  .contact-band { position: absolute; left: 0; top: 0; width: 600px; height: 343px; }
  .contact-list {
    position: absolute; left: 0; right: 0; top: 218px;
    display: flex; flex-direction: column; align-items: center; gap: 8px;
    padding-left: 40px;
    font-family: "Source Sans 3", sans-serif;
    color: var(--white);
  }
  .contact-line { display: flex; align-items: center; gap: 8px; }
  .contact-phone { font-size: 19px; }
  .contact-email { font-size: 15px; }
  .contact-address { font-size: 16px; margin-top: 4px; }
  .contact-icon { width: 14px; height: 16px; flex: none; }
</style>
</head>
<body>
  <main class="sheet">
    <section class="card card-front" aria-label="Card front">
      <div class="brand"><span class="brand-dot"></span><span class="brand-name">galavoyant</span></div>
      <p class="website">www.galavoyant.com</p>
    </section>

    <section class="card card-back" aria-label="Card back">
      <svg class="contact-band" viewBox="0 0 600 343" aria-hidden="true">
        <path d="M0,318 C110,210 330,160 600,200 L600,343 L0,343 Z" fill="var(--teal)"/>
        <path d="M0,312 C110,204 330,154 600,194" fill="none" stroke="var(--ink)" stroke-width="2"/>
      </svg>
      <div class="brand"><span class="brand-dot"></span><span class="brand-name">galavoyant</span></div>
      <p class="holder-name">Lorna Pettibone</p>
      <div class="contact-list">
        <p class="contact-line contact-phone">
          <svg class="contact-icon" viewBox="0 0 14 18" aria-hidden="true">
            <rect x="2" y="1" width="10" height="16" rx="2" fill="none" stroke="var(--white)" stroke-width="1.6"/>
            <rect x="4" y="4" width="6" height="5" fill="var(--white)"/>
            <circle cx="7" cy="13.5" r="1.2" fill="var(--white)"/>
          </svg>
          202.481.7730
        </p>
        <p class="contact-line contact-email">
          <svg class="contact-icon" viewBox="0 0 16 12" aria-hidden="true">
            <rect x="1" y="1" width="14" height="10" fill="none" stroke="var(--white)" stroke-width="1.5"/>
            <path d="M1,1 L8,7 L15,1" fill="none" stroke="var(--white)" stroke-width="1.5"/>
          </svg>
          lpettibone@galavoyant.com
        </p>
        <p class="contact-line contact-address">PO Box 318, Washington, DC 20019</p>
      </div>
    </section>
  </main>
</body>
</html>
```